Flyer for Children Therapy Center

We need a flyer with front and back with the following services:

Services:
- Entre outros!

Products:

Target Market(s)

Parents of children with special needs

Colors

Designer to choose colors to be used in the design.

Requirements
Must have
• The flyer must have:
• - Our logo
• - Company Name: Raiz Doce Luz
• - center description: Centro de Terapias Especializadas para crianças e jovens.
• - Slogan: Semeamos amor, colhemos sorrisos, distribuímos vitórias!
• - Site: www.ramolu.pt
• - Facebook: www.facebook.com/raizdoceluz
• - Cellular phone: +351 915 487 062
• - Land Line: +351 218 640 275
• - E-mail: geral@ramolu.pt
• - Address: R. Fernando Queirós Pimentel 3B, 2610-187 - Póvoa de Santa Iria, Portugal
Nice to have
• Logo colors
Should not have
• Dark colors.

```html
<!DOCTYPE html>
<html lang="pt">
<head>
<meta charset="utf-8">
<title>Raiz Doce Luz — Flyer</title>
<link href="https://fonts.googleapis.com/css2?family=Open+Sans:wght@400;600;700&display=swap" rel="stylesheet">
<style>
:root{
  --bg:#ececec;
  --paper:#ffffff;
  --teal:#1fa6b3;
  --teal-dark:#0f6f79;
  --teal-mid:#15909b;
  --teal-light:#5ec4cd;
  --ink:#14545e;
  --text:#555c5e;
  --muted:#8a8f91;
  --photo-a:#c98b5c;
  --photo-b:#7a4a2f;
}
*{margin:0;padding:0;box-sizing:border-box}
html,body{width:1200px;height:3005px;overflow:hidden}
body{background:var(--bg);font-family:"Open Sans",Arial,sans-serif;color:var(--text);position:relative}
.side-label{position:absolute;left:254px;font-size:17px;font-weight:600;color:#8d9193;letter-spacing:.5px}
.page{position:absolute;left:254px;width:692px;height:894px;background:var(--paper);box-shadow:0 3px 14px rgba(0,0,0,.18);overflow:hidden}
.page svg.shapes{position:absolute;left:0;top:0}
.abs{position:absolute}

/* front */
.logo-dot{position:absolute;left:60px;top:50px;width:72px;height:72px;border-radius:50%;background:var(--paper)}
.slogan-1{left:52px;top:322px;font-size:33px;color:var(--teal);font-weight:400;letter-spacing:.5px}
.slogan-2{left:52px;top:368px;font-size:25px;color:var(--ink);line-height:34px}
.tagline{left:52px;top:446px;font-size:21px;color:#444;line-height:27px}
.section-title{font-size:17px;font-weight:700;color:var(--teal);letter-spacing:.5px}
.body-copy{font-size:11px;line-height:16.5px;color:var(--text);text-align:justify;width:354px}
.divider{left:412px;top:510px;width:1px;height:380px;background:#dcdcdc;box-shadow:3px 0 6px rgba(0,0,0,.08)}
.brand-name{font-size:21px;color:var(--ink);font-weight:600}
.service-list{list-style:none;left:456px;top:632px;width:220px}
.service-list li{position:relative;padding-left:30px;font-size:16px;color:#3d4b4e;line-height:22px;margin-bottom:10px}
.service-list li::before{content:"";position:absolute;left:2px;top:8px;width:7px;height:7px;border-radius:50%;background:var(--teal)}
.extra{left:486px;top:822px;font-size:14px;color:var(--muted)}

/* back */
.item{position:absolute;display:flex;gap:14px}
.thumb{flex:none;width:94px;height:64px;background:linear-gradient(135deg,#e9b77c,#4f8bb5 60%,#d6d2cc)}
.item-title{font-size:15.5px;font-weight:600;color:var(--ink);line-height:20px}
.item-text{font-size:10px;line-height:13px;color:var(--muted);margin-top:3px;width:140px}
.back-slogan{left:400px;top:552px;width:330px;text-align:center;color:var(--ink);font-size:18px;line-height:25px}
.back-slogan .lead{font-size:23px;color:var(--teal)}
.contact{left:52px;top:720px;font-size:11.5px;line-height:16px;color:#4a4f51}
.contact dt{font-weight:700;color:#333}
.contact dd{margin-bottom:10px}
.social-box{left:484px;top:776px;width:28px;height:28px;background:var(--paper);opacity:.9}
.web{left:380px;width:260px;text-align:center;color:#fff}
</style>
</head>
<body>

<div class="side-label" style="top:784px">FRONTSIDE</div>

<section class="page front" style="top:890px">
  <svg class="shapes" width="692" height="894" viewBox="0 0 692 894">
    <defs>
      <linearGradient id="frontPhoto" x1="0" y1="0" x2="1" y2="1">
        <stop offset="0" stop-color="#d9c7a8"/>
        <stop offset=".5" stop-color="var(--photo-a)"/>
        <stop offset="1" stop-color="var(--photo-b)"/>
      </linearGradient>
    </defs>
    <rect x="0" y="0" width="692" height="470" fill="var(--teal-mid)"/>
    <polygon points="0,0 230,0 0,230" fill="var(--teal)"/>
    <polygon points="0,230 230,0 270,170 0,336" fill="var(--teal-dark)" opacity=".85"/>
    <polygon points="120,0 230,0 175,60" fill="var(--teal-light)"/>
    <g role="img" aria-label="Photo: a smiling therapist and a girl with glasses playing a guitar together">
      <polygon points="230,0 692,0 692,470 560,470 270,170" fill="url(#frontPhoto)"/>
    </g>
    <polygon points="230,0 430,0 330,100" fill="var(--teal)" opacity=".8"/>
    <polygon points="0,336 270,170 560,470 692,470 692,894 0,894" fill="var(--paper)"/>
    <polygon points="692,826 692,894 622,894" fill="var(--teal)"/>
    <polygon points="692,800 692,850 650,850" fill="var(--teal-light)" opacity=".7"/>
  </svg>
  <div class="logo-dot"></div>

  <h1 class="abs slogan-1">SEMEAMOS AMOR,</h1>
  <p class="abs slogan-2">COLHEMOS SORRISOS,<br>DISTRIBUÍMOS VITÓRIAS!</p>
  <p class="abs tagline">Centro de Terapias Especializadas<br>para crianças e jovens.</p>

  <h2 class="abs section-title" style="left:52px;top:528px">ABOUT &nbsp;US</h2>
  <p class="abs body-copy" style="left:52px;top:558px">Somos um centro dedicado ao desenvolvimento de crianças e jovens, com uma equipa multidisciplinar que acompanha cada família de perto. Acreditamos que cada pequena conquista merece ser celebrada, e trabalhamos todos os dias para criar um espaço seguro, alegre e acolhedor onde cada criança possa crescer ao seu ritmo e descobrir o melhor de si.</p>

  <h2 class="abs section-title" style="left:52px;top:698px">OUR MISSION</h2>
  <p class="abs body-copy" style="left:52px;top:728px">A nossa missão é promover a autonomia e o bem-estar de cada criança através de terapias personalizadas, baseadas em evidência e feitas com carinho. Queremos apoiar as famílias em todas as etapas, partilhando ferramentas e esperança para o dia a dia.</p>

  <div class="abs divider"></div>

  <p class="abs brand-name" style="left:456px;top:560px">Raiz Doce Luz</p>
  <h2 class="abs section-title" style="left:456px;top:598px">OUR SERVICES</h2>
  <ul class="abs service-list">
    <li>Fisioterapia</li>
    <li>Terapia Ocupacional</li>
    <li>Terapia da Fala</li>
    <li>Musicoterapia</li>
    <li>Estimulação Elétrica Neurofuncional</li>
  </ul>
  <p class="abs extra">Entre outros!</p>
</section>

<div class="side-label" style="top:1852px">BACKSIDE</div>

<section class="page back" style="top:1904px">
  <svg class="shapes" width="692" height="894" viewBox="0 0 692 894">
    <defs>
      <linearGradient id="backPhoto" x1="0" y1="0" x2="1" y2="1">
        <stop offset="0" stop-color="#f2f2f2"/>
        <stop offset="1" stop-color="#cfcfcf"/>
      </linearGradient>
    </defs>
    <polygon points="0,0 70,0 0,60" fill="var(--teal)"/>
    <g role="img" aria-label="Faded photo of a smiling therapist with a child">
      <polygon points="0,556 400,556 560,716 560,894 0,894" fill="url(#backPhoto)"/>
    </g>
    <polygon points="692,560 692,894 380,894 540,720" fill="var(--teal-mid)"/>
    <polygon points="692,600 692,894 396,894" fill="var(--teal-dark)"/>
    <polygon points="180,894 336,740 492,894" fill="var(--teal-light)" opacity=".85"/>
    <polygon points="336,740 492,894 560,820" fill="var(--teal)" opacity=".7"/>
  </svg>

  <h2 class="abs section-title" style="left:54px;top:50px">OUR SERVICES</h2>
  <div class="item" style="left:54px;top:92px"><div class="thumb" role="img" aria-label="Physiotherapy session photo"></div><div><p class="item-title">Fisioterapia</p><p class="item-text">Sessões individuais adaptadas a cada criança e família.</p></div></div>
  <div class="item" style="left:54px;top:178px"><div class="thumb" role="img" aria-label="Occupational therapy photo"></div><div><p class="item-title">Terapia Ocupacional</p><p class="item-text">Atividades diárias que reforçam a autonomia com alegria.</p></div></div>
  <div class="item" style="left:54px;top:264px"><div class="thumb" role="img" aria-label="Speech therapy photo"></div><div><p class="item-title">Terapia da Fala</p><p class="item-text">Comunicação, linguagem e confiança trabalhadas passo a passo.</p></div></div>
  <div class="item" style="left:54px;top:350px"><div class="thumb" role="img" aria-label="Music therapy photo"></div><div><p class="item-title">Musicoterapia</p><p class="item-text">A música como ponte para expressão e ligação.</p></div></div>
  <div class="item" style="left:54px;top:436px"><div class="thumb" role="img" aria-label="Electrical stimulation therapy photo"></div><div><p class="item-title">Estimulação Elétrica<br>Neurofuncional</p><p class="item-text">Técnica segura que apoia o movimento e força.</p></div></div>

  <h2 class="abs section-title" style="left:368px;top:50px">OUR PRODUCTS</h2>
  <div class="item" style="left:368px;top:92px"><div class="thumb" style="width:96px;height:76px;background:linear-gradient(135deg,#f4f4ef,#d9e2cf)" role="img" aria-label="Herbal product label"></div><div><p class="item-title">Fitoterapia Tradicional Chinesa</p><p class="item-text">Soluções naturais escolhidas com cuidado e rigor.</p></div></div>
  <div class="item" style="left:368px;top:190px"><div class="thumb" style="width:96px;height:76px" role="img" aria-label="Dynamic orthoses photo"></div><div><p class="item-title">Ortóteses dinâmicas funcionais</p><p class="item-text">Apoio confortável feito à medida de cada corpo.</p></div></div>
  <div class="item" style="left:368px;top:284px"><div class="thumb" style="width:96px;height:76px" role="img" aria-label="Compression suit photo"></div><div><p class="item-title">Fato de compressão dinâmica sob medida</p><p class="item-text">Estabilidade e postura para cada desafio do dia.</p></div></div>
  <div class="item" style="left:368px;top:378px"><div class="thumb" style="width:96px;height:76px" role="img" aria-label="Pelvic seat photo"></div><div><p class="item-title">Assento pélvico moldado com técnica exclusiva</p><p class="item-text">Conforto e alinhamento pensados para longas horas.</p></div></div>

  <p class="abs back-slogan"><span class="lead">SEMEAMOS AMOR,</span><br>COLHEMOS SORRISOS,<br>DISTRIBUÍMOS<br>VITÓRIAS!</p>

  <p class="abs brand-name" style="left:52px;top:666px;color:#3d4548">Raiz Doce Luz</p>
  <dl class="abs contact">
    <dt>Address</dt>
    <dd>R. Fernando Queirós Pimentel 3B,<br>2610-187 - Póvoa de Santa Iria, Portugal</dd>
    <dd>Cell: +351 915 487 062</dd>
    <dd>Land Line: +351 218 640 275</dd>
    <dd>E-mail: geral@ramolu.pt</dd>
  </dl>

  <div class="abs social-box"></div>
  <p class="abs web" style="top:816px;font-size:10.5px">www.facebook.com/raizdoceluz</p>
  <p class="abs web" style="top:834px;font-size:15px;font-weight:600">www.ramolu.pt</p>
</section>

</body>
</html>
```